Napa Winery - Chardonnay wine label

We are looking for a label for a new Napa Valley winery - chardonnay wine. The winery is "Marrowbrook Hill Vintners" and we would like to see it depicted on a white wine (chardonnay style) bottle. The winery is called Marrowbrook Hill Vintners.

We are open to ideas!

Target Market(s)

High-end chardonnay lovers

Requirements
Nice to have
• Painted or etched label onto bottle

```html
<!DOCTYPE html>
<html lang="en">
<head>
<meta charset="utf-8">
<title>Halcyon Meridian Chardonnay Label</title>
<link href="https://fonts.googleapis.com/css2?family=Marcellus&family=Pinyon+Script&family=Archivo+Narrow:wght@400;700&display=swap" rel="stylesheet">
<style>
  :root {
    --paper: #ffffff;
    --ink-grey: #5a5b5d;
    --ink-dark: #3a3a3c;
    --gold: #b09643;
    --band: #bdbec0;
    --band-text: #ffffff;
    --etch-dark: #6e6e6e;
    --etch-light: #d9d9d9;
  }
  html, body {
    margin: 0;
    padding: 0;
    width: 1200px;
    height: 1169px;
    overflow: hidden;
    background: var(--paper);
  }
  .label {
    position: absolute;
    left: 0;
    top: 0;
    width: 1200px;
    height: 1169px;
    display: flex;
    flex-direction: column;
    align-items: center;
    justify-content: center;
  }
  .vineyard-scene {
    display: block;
    width: 300px;
    height: 130px;
  }
  .wine-name {
    margin-top: 34px;
    display: flex;
    align-items: baseline;
    line-height: 1;
    white-space: nowrap;
  }
  .wine-name__first {
    font-family: "Marcellus", serif;
    font-size: 44px;
    letter-spacing: 4px;
    color: var(--ink-grey);
  }
  .wine-name__second {
    font-family: "Pinyon Script", cursive;
    font-size: 78px;
    color: var(--gold);
    margin-left: 2px;
  }
  .varietal-band {
    margin-top: 16px;
    width: 555px;
    height: 58px;
    background: var(--band);
    display: flex;
    align-items: center;
    justify-content: center;
  }
  .varietal-band__text {
    font-family: "Archivo Narrow", sans-serif;
    font-weight: 700;
    font-size: 25px;
    letter-spacing: 5px;
    color: var(--band-text);
  }
  .producer {
    margin-top: 40px;
    text-align: center;
    font-family: "Archivo Narrow", sans-serif;
    font-size: 22px;
    line-height: 1.3;
    color: var(--ink-dark);
  }
  .producer p { margin: 0; }
</style>
</head>
<body>
  <main class="label">
    <svg class="vineyard-scene" viewBox="0 0 300 130" role="img" aria-label="Etched vineyard landscape with rolling hills, rows of vines and a farmhouse">
      <defs>
        <radialGradient id="etch-fade" cx="50%" cy="50%" r="50%">
          <stop offset="0%" stop-color="var(--etch-dark)" stop-opacity="0.85"/>
          <stop offset="55%" stop-color="var(--etch-dark)" stop-opacity="0.55"/>
          <stop offset="85%" stop-color="var(--etch-light)" stop-opacity="0.5"/>
          <stop offset="100%" stop-color="var(--etch-light)" stop-opacity="0"/>
        </radialGradient>
      </defs>
      <ellipse cx="150" cy="65" rx="150" ry="65" fill="url(#etch-fade)"/>
    </svg>

    <h1 class="wine-name">
      <span class="wine-name__first">HALCYON</span><span class="wine-name__second">Meridian</span>
    </h1>

    <div class="varietal-band">
      <span class="varietal-band__text">CHARDONNAY</span>
    </div>

    <div class="producer">
      <p>Napa Valley Winery</p>
      <p>Marrowbrook Hill Vintners</p>
    </div>
  </main>
</body>
</html>
```